5 Planner Covers for Teacher Planners

Hello,
I currently run a Speech-Language Pathologist website and have created a planner for my fellow Speech Therapist. I would like someone to create 5 different planner covers so my followers will have different options to choose from.
Here is my planner from last year to give you an idea of what the planner will look like http://www.talkbloomshop.example/free-slp-planner/
My followers are mostly women aged 25-50. However, I don't want the covers to be overly girly or excessive with flowers. Simple is better.
I'd also like there to be an editable text box to allow the Speech Therapist to type their name on their cover if they wish.
Planner Cover can say any of the following: SLP Planner, Planner, Speech Therapy Planner, Speech-Language Pathologist (maybe this title could be editable as well??).
To give you an idea I have uploaded a screenshot of last year's planners cover that I made myself.
What I am looking for:
-Size 8.5" by 11"
-5 different planner covers
-1 gender-neutral cover
-simple design
-limited flowers (or overly girly
-text box to add a personal name
-Possible titles: SLP Planner, Planner, Speech Therapy Planner, Speech-Language Pathologist (maybe this title could be editable as well??)
Target Market(s)
Women aged 25-50
Colors
Designer to choose colors to be used in the design.
Requirements
Must have
- What I am looking for:
-Size 8.5" by 11"
-1 gender-neutral cover
-simple design
Nice to have
- I've uploaded some that I like from Craftora to give you an idea.
Here is my craftora store https://www.craftora.example/shop/QuietMeadowHome to give you an idea of things I like.
I like Marla Pendry and her simple elegant rustic style.

```html
<!DOCTYPE html>
<html lang="en">
<head>
<meta charset="utf-8">
<title>SLP Planner Cover</title>
<link href="https://fonts.googleapis.com/css2?family=Sacramento&family=Dancing+Script:wght@700&display=swap" rel="stylesheet">
<style>
  :root {
    --plum-black: #170914;
    --plum-deep: #24101f;
    --plum-mid: #3b1736;
    --violet: #5a2660;
    --magenta: #9a3f8e;
    --orchid: #b0509e;
    --rose: #d97aa8;
    --white: #ffffff;
  }
  html, body {
    margin: 0;
    padding: 0;
    width: 928px;
    height: 1200px;
    overflow: hidden;
    background: var(--plum-black);
  }
  .cover {
    position: relative;
    width: 928px;
    height: 1200px;
    overflow: hidden;
  }
  .cover-backdrop {
    position: absolute;
    inset: 0;
    background:
      radial-gradient(ellipse 260px 240px at 90px 1000px, rgba(217,122,168,0.85), transparent 75%),
      radial-gradient(ellipse 380px 260px at 300px 1000px, rgba(176,80,158,0.55), transparent 75%),
      radial-gradient(ellipse 300px 360px at 620px 420px, rgba(176,80,158,0.6), transparent 72%),
      radial-gradient(ellipse 360px 260px at 780px 300px, rgba(154,63,142,0.45), transparent 72%),
      radial-gradient(ellipse 420px 320px at 700px 760px, rgba(90,38,96,0.7), transparent 75%),
      radial-gradient(ellipse 400px 200px at 740px 1120px, rgba(90,38,96,0.5), transparent 75%),
      linear-gradient(150deg, var(--plum-black) 0%, var(--plum-deep) 38%, var(--plum-mid) 70%, var(--plum-deep) 100%);
  }
  .name-plate {
    position: absolute;
    left: 224px;
    top: 482px;
    width: 451px;
    height: 224px;
  }
  .name-plate svg {
    position: absolute;
    inset: 0;
  }
  .plate-outer {
    fill: none;
    stroke: var(--white);
    stroke-width: 6;
  }
  .plate-inner {
    fill: none;
    stroke: var(--white);
    stroke-width: 2.5;
  }
  .plate-title {
    position: absolute;
    left: 0;
    right: 0;
    top: 40px;
    margin: 0;
    text-align: center;
    font-family: "Sacramento", cursive;
    font-weight: 400;
    font-size: 56px;
    line-height: 1;
    color: var(--white);
  }
  .plate-belongs {
    position: absolute;
    left: 0;
    right: 0;
    top: 110px;
    margin: 0;
    text-align: center;
    font-family: "Dancing Script", cursive;
    font-weight: 700;
    font-size: 25px;
    line-height: 1;
    color: var(--white);
  }
  .plate-name-line {
    position: absolute;
    left: 108px;
    top: 180px;
    width: 235px;
    height: 2px;
    background: var(--white);
  }
</style>
</head>
<body>
  <main class="cover">
    <div class="cover-backdrop" role="img" aria-label="Low-poly geometric facets in deep plum, violet, magenta and rose tones"></div>

    <section class="name-plate">
      <svg viewBox="0 0 451 224" width="451" height="224" aria-hidden="true">
        <path class="plate-outer" d="M70,4 H381 Q398,40 428,48 Q448,112 428,176 Q398,184 381,220 H70 Q53,184 23,176 Q3,112 23,48 Q53,40 70,4 Z"/>
        <path class="plate-inner" d="M76,14 H375 Q390,48 419,57 Q435,112 419,167 Q390,176 375,210 H76 Q61,176 32,167 Q16,112 32,57 Q61,48 76,14 Z"/>
      </svg>
      <h1 class="plate-title">SLP Planner</h1>
      <p class="plate-belongs">belongs to</p>
      <div class="plate-name-line"></div>
    </section>
  </main>
</body>
</html>
```